Home and interior page website design for HVAC company - Veltrix Corp.

Create homepage and one interior page website design for an HVAC (Heating and AC) company. Current website is: https://veltrixcorp-example.com/.

Client has specifically asked that the new site look inviting, informative and interactive. They mentioned that the logo on a white background doesn't look appealing and would like to see other options. (I have included the white background one from their current website as well as the one on an image that the client sent me) The site must include their financing widget (we have the code for this) in a prominent place. Image can be found here: https://fundlarkpay-example.com/badges/fundlark-financing.png.

The content from their existing site belongs to the company that built their site and have said we cannot use any of it. This development site (http://veltrixwebd.qmzdev-example.com/) is what we originally created from our template for them before they decided they wanted a custom built site. The content there is what will need to be on the new home page.

We have gathered images from the client that they would like used throughout the site in this folder: https://files.brelvon-example.com/shared/folder/Xk4pQ9wLmZ2rTn7vBc8HyD5sJf3GaE6uWq1NoKi0RtYe?e=7PLWQD. They would like the photos used to be in tune with the topic being spoken about so if the topic is maintenance on a central AC system the photo used to lead that topic should be of a unit being cleaned.

For the testimonials section please also include a button or "Click here for more testimonials" as requested by the client.

Top Level NAV should include: Home, Residential, Commercial, Testimonials, Gallery, About Us, Coupons, Contact Us

For the interior page, we're looking for the same inviting, informative and interactive feel to the site, preferably with a banner of some sort and the form close to the top of the page if not able to keep it above the fold in the banner. Page should also include sections with clients images used to avoid a wall of text.

Example Websites that the client likes:
https://www.corvalheatcoolinc-example.com/
https://www.frostelmg-example.com/?ref=Q8mZt3LpXw2NvB7cRk5YhJ1sDf4GaE9u
https://www.glimtherm-example.com/nny/
https://www.ubrix-example.com/
https://otterclimateny-example.com/

• *Summarized from project description:
-financing image in prominent place
-content from development site
-images from clients folder
-button or "click here.." note in testimonials section
-form above the fold
-logo not on white background

```html
<!DOCTYPE html>
<html lang="en">
<head>
<meta charset="utf-8">
<title>Veltrix Mechanical Contractors — Residential and Commercial HVAC</title>
<link rel="stylesheet" href="https://fonts.googleapis.com/css2?family=Montserrat:wght@400;500;600;700;800&display=swap">
<style>
:root{
  --coral:#f96b64;
  --coral-soft:#fde3e1;
  --slate:#465661;
  --slate-dark:#3d4b55;
  --ink:#1f1f1f;
  --text:#555;
  --mist:#f2f2f2;
  --white:#fff;
}
*{box-sizing:border-box;margin:0;padding:0}
html,body{width:1200px;height:4501px;overflow:hidden}
body{position:relative;background:var(--white);font-family:'Montserrat',sans-serif;color:var(--text)}
.abs{position:absolute}
.photo{position:absolute}

/* header */
.site-header{position:absolute;left:0;top:0;width:1200px;height:90px}
.brand{position:absolute;left:65px;top:10px;display:flex;align-items:center;gap:10px}
.brand-name{font-weight:800;font-size:30px;color:var(--ink);letter-spacing:2px;line-height:1}
.brand-mark{width:26px;height:26px;border-radius:50%;background:var(--ink)}
.brand-sub{position:absolute;left:65px;top:52px;font-size:9px;letter-spacing:1px;color:var(--ink);font-weight:600}
.main-nav{position:absolute;left:318px;top:19px;display:flex;gap:24px;font-size:12px}
.main-nav a{color:#666;text-decoration:none;white-space:nowrap}
.main-nav a.active{color:var(--coral)}
.btn-consult{position:absolute;left:964px;top:8px;width:177px;height:37px;background:var(--slate);color:#fff;font-size:12px;font-weight:600;display:flex;align-items:center;justify-content:center;border-radius:3px}

/* hero */
.hero{position:absolute;left:0;top:91px;width:1200px;height:622px;background:var(--mist);overflow:hidden}
.hero-photo{left:0;top:0;width:1200px;height:622px;background:linear-gradient(135deg,#5f6062,#8a8b8c 50%,#3e3f42);clip-path:polygon(525px 0,100% 0,100% 100%,402px 100%)}
.hero-panel{left:0;top:66px;width:615px;height:472px;background:var(--coral);clip-path:polygon(0 0,615px 0,480px 472px,0 472px)}
.hero-title{position:absolute;left:62px;top:150px;color:#fff;font-weight:700;font-size:44px;line-height:60px}
.hero-cta{position:absolute;left:83px;top:370px;color:#fff;font-size:12px;font-weight:600}
.finance-widget{position:absolute;left:83px;top:412px;width:190px;height:54px;background:#fff;border-radius:6px;box-shadow:0 4px 12px rgba(0,0,0,.15)}

/* about */
.about-frame{left:248px;top:832px;width:325px;height:370px;border:1px solid #eee;background:#fff;box-shadow:0 0 14px rgba(0,0,0,.06)}
.about-img-a{left:73px;top:840px;width:300px;height:340px;background:#fff;box-shadow:0 0 14px rgba(0,0,0,.12);padding:10px}
.about-img-a div{width:100%;height:100%;background:linear-gradient(160deg,#8c7a66,#4b4e55 60%,#b89a6a)}
.about-img-b{left:280px;top:896px;width:268px;height:230px;background:#fff;box-shadow:0 0 14px rgba(0,0,0,.12);padding:8px}
.about-img-b div{width:100%;height:100%;background:linear-gradient(140deg,#7d8894,#a1a8b0 45%,#d88a3c)}
.about-deco{left:1010px;top:836px;width:190px;height:220px;background:var(--coral-soft);clip-path:polygon(0 50%,62% 0,100% 30%,100% 100%)}
.h2{font-weight:700;color:var(--ink);font-size:29px}
.h2 span{color:var(--coral)}
.about-title{position:absolute;left:613px;top:840px}
.about-lead{position:absolute;left:614px;top:906px;width:370px;font-size:12px;font-weight:600;color:var(--ink);line-height:19px}
.about-body{position:absolute;left:613px;top:972px;width:500px;font-size:11.3px;line-height:19.5px}
.about-body p+p{margin-top:12px}

/* band */
.band-slate{left:0;top:1371px;width:1200px;height:504px;background:var(--slate)}
.band-light{left:0;top:1302px;width:868px;height:148px;background:#f3f3f3;clip-path:polygon(0 0,868px 0,780px 148px,0 148px)}
.band-title{position:absolute;left:61px;top:1342px;font-size:25px;font-weight:600;color:var(--ink);line-height:34px}
.services-title{position:absolute;left:0;width:1358px;top:1514px;text-align:center;color:#fff;font-size:29px;font-weight:600}
.service{position:absolute;width:240px;text-align:center;color:#fff}
.service .ring{width:112px;height:112px;margin:0 auto;border-radius:50%;background:#fff;display:flex;align-items:center;justify-content:center;box-shadow:0 0 0 4px rgba(255,255,255,.15)}
.service h3{font-size:14px;font-weight:600;margin-top:12px}
.service p{font-size:11.3px;line-height:19px;margin-top:4px}

/* ac */
.ac-title{position:absolute;left:103px;top:1982px;font-size:30px;line-height:38px}
.ac-sub{position:absolute;left:103px;top:2064px;font-size:11px;line-height:19px;color:var(--ink)}
.ac-list{position:absolute;left:103px;top:2118px;list-style:none;font-size:11.3px}
.ac-list li{height:30px}
.btn-slate{position:absolute;background:var(--slate);color:#fff;font-size:12px;font-weight:500;display:flex;align-items:center;justify-content:center;border-radius:3px}
.ac-img-tall{left:571px;top:1957px;width:285px;height:375px;background:linear-gradient(170deg,#9cb8c4,#7a4a3a 40%,#5a3b30)}
.ac-img-top{left:879px;top:1957px;width:225px;height:225px;background:linear-gradient(180deg,#aebfd4,#c9ccd0 55%,#8f9398)}
.ac-badge{left:879px;top:2205px;width:225px;height:119px;background:var(--coral);color:#fff;text-align:center;padding-top:22px}
.ac-badge strong{display:block;font-size:34px;font-weight:700;letter-spacing:1px}
.ac-badge span{font-size:13px}

/* day or night */
.night{position:absolute;left:0;top:2439px;width:1200px;height:562px;background:var(--slate);overflow:hidden}
.night-photo{left:0;top:0;width:1200px;height:562px;background:linear-gradient(120deg,#c9b9a3,#8a8e99 45%,#2f4b7c 80%,#e8e2d6);clip-path:polygon(398px 0,100% 0,100% 100%,253px 100%)}
.night-panel{left:0;top:63px;width:620px;height:419px;background:var(--coral);clip-path:polygon(0 0,620px 0,507px 419px,0 419px)}
.night-title{position:absolute;left:61px;top:133px;color:#fff;font-size:23px;font-weight:600;line-height:30px}
.night-body{position:absolute;left:61px;top:254px;width:410px;color:#fff;font-size:11px;line-height:19.3px}

/* gallery */
.gallery-title{position:absolute;left:0;width:1200px;top:3086px;text-align:center}
.g1{left:65px;top:3166px;width:262px;height:337px;background:linear-gradient(180deg,#b8c4d2,#7d92ad 60%,#4d6f93)}
.g2{left:335px;top:3152px;width:262px;height:337px;background:linear-gradient(160deg,#4a4d52,#d8c2ae 40%,#3a66b5 80%)}
.g3{left:604px;top:3166px;width:262px;height:337px;background:linear-gradient(170deg,#c9d3df,#9a9ea6 50%,#6b7078)}
.g4{left:874px;top:3166px;width:263px;height:337px;background:linear-gradient(180deg,#3d7bc9,#9fbfe0 40%,#d7d9dc 70%,#8d7a63)}

/* testimonial */
.testi-photo{left:0;top:3625px;width:1200px;height:425px;background:linear-gradient(120deg,#b5aca6,#e8d9cb 40%,#d2c4b8)}
.testi-panel{left:0;top:3625px;width:1200px;height:425px;background:#f5f5f5;clip-path:polygon(822px 50px,1200px 50px,1200px 425px,472px 425px)}
.testi-title{position:absolute;left:690px;top:3760px}
.testi-body{position:absolute;left:690px;top:3822px;width:340px;font-size:11px;line-height:19.5px}
.stars{position:absolute;left:690px;top:3954px;color:var(--coral);font-size:12px;letter-spacing:2px}
.testi-name{position:absolute;left:694px;top:3982px;font-size:12px;color:var(--ink);font-weight:500}
.btn-more{position:absolute;left:792px;top:3978px;width:160px;height:26px;background:var(--slate);color:#fff;font-size:10px;font-weight:600;display:flex;align-items:center;justify-content:center;border-radius:3px;letter-spacing:.3px}
.arrow-btn{position:absolute;top:3978px;width:33px;height:26px;border:1.5px solid var(--coral);display:flex;align-items:center;justify-content:center}
.arrow-btn.dark{border-color:var(--ink)}

/* footer */
.site-footer{position:absolute;left:0;top:4079px;width:1200px;height:372px;background:var(--slate);color:#fff}
.foot-brand{position:absolute;left:61px;top:50px;font-weight:800;font-size:30px;color:var(--coral);letter-spacing:2px}
.foot-brand-sub{position:absolute;left:61px;top:86px;font-size:9px;letter-spacing:1px;color:var(--coral);font-weight:600}
.pay-label{position:absolute;left:61px;top:145px;font-size:11px}
.pay{position:absolute;width:46px;height:28px;border-radius:4px;background:#fff}
.foot-col{position:absolute;top:66px}
.foot-col h4{font-size:17px;font-weight:600;margin-bottom:10px}
.foot-links{list-style:none;font-size:11px}
.foot-links li{height:30px;padding-left:15px;position:relative}
.foot-links li::before{content:"";position:absolute;left:0;top:4px;width:5px;height:5px;background:var(--coral);transform:rotate(45deg)}
.contact-item{position:relative;padding-left:32px;font-size:11px;line-height:24px;margin-bottom:20px}
.contact-item svg{position:absolute;left:0;top:3px}
.social-dot{position:absolute;left:0;top:6px;width:16px;height:16px;border-radius:50%;background:var(--coral)}
.copyright{position:absolute;left:0;top:4451px;width:1200px;height:50px;background:var(--coral);color:#fff;font-size:11px;text-align:center;line-height:50px}
</style>
</head>
<body>

<header class="site-header">
  <div class="brand"><span class="brand-name">VELTRIX</span><span class="brand-mark"></span></div>
  <div class="brand-sub">MECHANICAL CONTRACTORS</div>
  <nav class="main-nav">
    <a class="active" href="#">Home</a><a href="#">Residential</a><a href="#">Commercial</a><a href="#">Testimonials</a><a href="#">Gallery</a><a href="#">About Us</a><a href="#">Coupons</a><a href="#">Contact Us</a>
  </nav>
  <div class="btn-consult">GET FREE CONSULTING</div>
</header>

<section class="hero">
  <div class="photo hero-photo" role="img" aria-label="Outdoor mini-split condenser unit mounted on a grey sided wall below a lit window"></div>
  <div class="photo hero-panel"></div>
  <h1 class="hero-title">Residential and<br>Commercial HVAC<br>Solutions</h1>
  <div class="hero-cta">GET A QUOTE</div>
  <div class="finance-widget" role="img" aria-label="Financing widget badge"></div>
</section>

<section class="about">
  <div class="abs about-deco"></div>
  <div class="abs about-frame"></div>
  <div class="abs about-img-a"><div role="img" aria-label="Technician on a ladder working on ductwork in a basement"></div></div>
  <div class="abs about-img-b"><div role="img" aria-label="Technician installing a window air conditioner"></div></div>
  <h2 class="h2 about-title">About <span>&nbsp;Us</span></h2>
  <p class="about-lead">Veltrix Mechanical Air Duct, Insulation, Furnace, Air Conditioning repair and replacement company offers top repair services.</p>
  <div class="about-body">
    <p>We can resolve any issues that may arise within your home. Our Harlow HVAC (heating, ventilating, and air conditioning) technicians are experts at inspecting and repairing systems that are not cooling or heating properly. They specialize at everything from condensers, coils, air ducts, air filtration to complete AC installations and AC replacements with the best warranties. Need an annual tune-up up? Ask about our service membership. Annual</p>
    <p>This makes sure that you have what your home needs when you need it. Veltrix Mechanical can help with the ongoing maintenance of all of your important air conditioning and furnace equipment, as well as annual home inspections to help prevent major HVAC emergencies down the road.</p>
  </div>
</section>

<section class="services">
  <div class="abs band-slate"></div>
  <div class="abs band-light"></div>
  <h2 class="band-title">Need heating And Ac Maintenance Repair<br>Services</h2>
  <h2 class="services-title">Repaire &amp; Services</h2>
  <svg class="abs" style="left:0;top:1580px" width="1200" height="140" viewBox="0 0 1200 140" fill="none" stroke="#9aa6ae" stroke-width="1.2">
    <path d="M0 130 C80 100,110 80,164 71 S350 50,449 53 S640 90,741 85 S960 70,1034 76 S1160 60,1200 45"/>
  </svg>
  <div class="service" style="left:44px;top:1595px">
    <div class="ring"><svg width="64" height="50" viewBox="0 0 64 50" fill="none" stroke="#f96b64" stroke-width="2.2" stroke-linecap="round"><rect x="2" y="2" width="60" height="22" rx="4"/><path d="M10 17h44M18 32c2 4-2 8 0 12M26 32c2 4-2 8 0 12M34 32c2 4-2 8 0 12M48 30v14M42 34l12 6M54 34l-12 6"/></svg></div>
    <h3>Air Conditioning</h3>
    <p>Depend on us for timely, quality, and<br>affordable air conditioning service</p>
  </div>
  <div class="service" style="left:329px;top:1577px">
    <div class="ring"><svg width="50" height="60" viewBox="0 0 50 60" fill="none" stroke="#f96b64" stroke-width="2.2" stroke-linecap="round"><path d="M8 58V26M16 58V22M24 58V20M32 58V22M40 58V26M4 58h42"/><path d="M25 4c6 6 7 10 3 14-3 3-8 2-8-3 0-4 3-5 5-11z"/></svg></div>
    <h3>Heating</h3>
    <p>Depend on us for timely, quality, and<br>affordable air conditioning service</p>
  </div>
  <div class="service" style="left:621px;top:1609px">
    <div class="ring"><svg width="56" height="56" viewBox="0 0 56 56" fill="none" stroke="#f96b64" stroke-width="2.2" stroke-linecap="round"><path d="M8 48L34 22M40 6c-6 0-10 6-7 12l4 4c6 3 12-1 12-7l-6 4-5-5zM10 10l6 2 26 26 6 8-8-6-26-26z"/></svg></div>
    <h3>Repairs</h3>
    <p>Depend on us for timely, quality, and<br>affordable air conditioning service</p>
  </div>
  <div class="service" style="left:914px;top:1600px">
    <div class="ring"><svg width="60" height="52" viewBox="0 0 60 52" fill="none" stroke="#f96b64" stroke-width="2.2" stroke-linecap="round"><path d="M4 22L30 4l26 18"/><path d="M12 44V34l5-9h26l5 9v10zM12 44v5M48 44v5"/><circle cx="20" cy="38" r="3"/><circle cx="40" cy="38" r="3"/></svg></div>
    <h3>Serving your area</h3>
    <p>Depend on us for timely, quality, and<br>affordable air conditioning service</p>
  </div>
</section>

<section class="ac">
  <h2 class="h2 ac-title">Air Conditioning &amp;<br><span>Cooling</span></h2>
  <p class="ac-sub">Serving both Residential &amp; Commercial<br>Heating &amp; Air Conditioning Needs</p>
  <ul class="ac-list">
    <li>Air Purifier System</li>
    <li>HVAC Parts, Repair, Installation</li>
    <li>Ductless Systems</li>
    <li>HVAC Maintenance Tune Up and Inspection</li>
    <li>HVAC Replacement Cost and Installation</li>
    <li>Gas Furnace Installations</li>
  </ul>
  <div class="btn-slate" style="left:101px;top:2311px;width:128px;height:38px">LEARN MORE</div>
  <div class="photo ac-img-tall" role="img" aria-label="Brick apartment building with fire escapes and green bay windows"></div>
  <div class="photo ac-img-top" role="img" aria-label="Technician servicing rooftop HVAC units"></div>
  <div class="photo ac-badge"><strong>VELTRIX</strong><span>Mechanical Contractors</span></div>
</section>

<section class="night">
  <div class="photo night-photo" role="img" aria-label="Technician's hands connecting refrigerant manifold gauges to an outdoor unit"></div>
  <div class="photo night-panel"></div>
  <h2 class="night-title">Day or Night, 24/7, Count on Trusted<br>Service from Veltrix Mechanical<br>Contractors Corp</h2>
  <p class="night-body">we always ensure you're getting the most for your money. For trustworthy HVAC service and installation, consider us your go-to. Veltrix Mechanical can help with the ongoing maintenance of all of your important air conditioning and furnace equipment, as well as annual home inspections</p>
  <div class="btn-slate" style="left:61px;top:372px;width:127px;height:36px">CONTACT US</div>
</section>

<section class="gallery">
  <h2 class="h2 gallery-title">Photo <span>Gellary</span></h2>
  <div class="photo g1" role="img" aria-label="Industrial air handler fan inside a metal enclosure"></div>
  <div class="photo g2" role="img" aria-label="Technician in overalls inspecting a ceiling vent"></div>
  <div class="photo g3" role="img" aria-label="Worker installing a metal unit outside a restaurant storefront"></div>
  <div class="photo g4" role="img" aria-label="Frosted rooftop condenser units under a blue sky"></div>
</section>

<section class="testimonial">
  <div class="photo testi-photo" role="img" aria-label="Smiling family relaxing together on a sofa"></div>
  <div class="photo testi-panel"></div>
  <h2 class="h2 testi-title">What Our <span>Client Say</span></h2>
  <p class="testi-body">Thank you so much for doing such a wonderful job on our air conditioning unit. I am very happy with the service provided to me from Veltrix Mechanical Contractors. The staff gathers my information before helping me out to see what they could do for me. I am thankful for all of your help and services.</p>
  <div class="stars">★★★★★</div>
  <div class="testi-name">- Dorian P.</div>
  <a class="btn-more" href="#">MORE TESTIMONIALS</a>
  <div class="arrow-btn" style="left:973px"><svg width="10" height="14" viewBox="0 0 10 14" fill="none" stroke="#f96b64" stroke-width="1.6"><path d="M8 1L2 7l6 6"/></svg></div>
  <div class="arrow-btn dark" style="left:1019px"><svg width="10" height="14" viewBox="0 0 10 14" fill="none" stroke="#1f1f1f" stroke-width="1.6"><path d="M2 1l6 6-6 6"/></svg></div>
</section>

<footer class="site-footer">
  <div class="foot-brand">VELTRIX</div>
  <div class="foot-brand-sub">MECHANICAL CONTRACTORS</div>
  <div class="pay-label">Payment Acceptable</div>
  <div class="pay" style="left:61px;top:181px"></div>
  <div class="pay" style="left:116px;top:181px"></div>
  <div class="pay" style="left:171px;top:181px"></div>
  <div class="pay" style="left:61px;top:225px"></div>
  <div class="pay" style="left:116px;top:225px"></div>
  <div class="pay" style="left:171px;top:225px"></div>

  <div class="foot-col" style="left:337px">
    <h4>Links</h4>
    <ul class="foot-links">
      <li>Home</li><li>Residential</li><li>Commercial</li><li>Testimonials</li><li>Gallery</li><li>About Us</li><li>Coupons</li><li>Contact Us</li>
    </ul>
  </div>

  <div class="foot-col" style="left:613px">
    <h4>Contact Us</h4>
    <div class="contact-item"><svg width="16" height="20" viewBox="0 0 16 20" fill="none" stroke="#f96b64" stroke-width="1.8"><path d="M8 19s6-7 6-11A6 6 0 0 0 2 8c0 4 6 11 6 11z"/><circle cx="8" cy="8" r="2"/></svg>Location<br>Harlow, NY 10482</div>
    <div class="contact-item"><svg width="18" height="14" viewBox="0 0 18 14" fill="#f96b64"><path d="M0 0h18v14H0z"/><path d="M1 1l8 6 8-6" fill="none" stroke="#465661" stroke-width="1.4"/></svg>Call Us<br>(555) 014-2297</div>
    <div class="contact-item"><svg width="16" height="16" viewBox="0 0 16 16" fill="#f96b64"><path d="M3 0l3 4-2 2c1 2 4 5 6 6l2-2 4 3-2 3C7 16 0 9 0 3z"/></svg>Email Us<br>veltrixcorp@mail-example.com</div>
  </div>

  <div class="foot-col" style="left:889px">
    <h4>Follow Us</h4>
    <div class="contact-item"><span class="social-dot"></span>Like Us On<br>Veltrix Social</div>
    <div class="contact-item"><span class="social-dot"></span>Like Us On<br>Veltrix Photos</div>
  </div>
</footer>
<div class="copyright">©2021, Veltrix Mechanical Contractors Corp- All Right Reserved.</div>

</body>
</html>
```